依頼概要
■依頼の目的/概要
森川拓郎商会は主に古紙のリサイクル事業をしております。
数年前に新たにブランドカラーが決定しましたが、
社内調査の結果、それらがお取引先の企業様に浸透していないことが分かりました。

そこでお取引先様にお渡しするノベルティの作成をお願いします。
お渡しは弊社の工場見学後などを想定しております。

■依頼詳細
今回はノベルティとして、オリジナルエコバッグの作成を企画しております。

■会社詳細
社名:「株式会社森川拓郎商会」
業種:古紙リサイクル業

■ノベルティ詳細
ノベルティ:エコバッグ
発注枚数:約50枚

■重視するポイント
当社のブランドイメージで作成いただきたく存じます。
当社のパッカー車(回収者)のイラストをいれていただきたいです。
参考までに画像添付させていただきます。
---------------------------------------------------------
「知性とセンスで環境問題を解決へと導く
「スマートなリサイクルカンパニー」

その他何かご不明な点がございましたら、お気軽にご質問下さい。
よろしくお願いいたします。
■ 選んだ理由

弊社のブランドカラーをうまく取り入れ、
「環境問題」と「その解決」の架け橋という発想でデザインを作成いただきました。
お客様に配布するもののため意味の込められたメッセージ性のあるデザインを選ばせていただきました。

■ 提案者全員のお礼・コメント

この度は素敵なデザインを作成いただき誠にありがとうございます。
どのデザインも素晴らしく選ぶのに大変お時間が掛かってしまいました。
今後も別件でデザインを依頼することもあるかと思います。
その際にはイメージにあった方については個別にお声がけさせて頂きたく存じます。

デザイン選定にお時間を頂戴し大変申し訳ございませんでした。
お忙しい中、ご協力いただきまして誠にありがとうございました。

```html
<!DOCTYPE html>
<html lang="ja">
<head>
<meta charset="UTF-8">
<title>森川拓郎商会 エコバッグ</title>
<link rel="stylesheet" href="https://fonts.googleapis.com/css2?family=Zen+Old+Mincho:wght@900&family=Noto+Sans+JP:wght@500&family=EB+Garamond:ital,wght@1,400&display=swap">
<style>
  :root {
    --paper: #ffffff;
    --ink: #000000;
    --inverse: #ffffff;
    --brand-green: #3fb34f;
    --truck-tone: #3c3c3c;
  }
  html, body {
    margin: 0;
    padding: 0;
    overflow: hidden;
  }
  body {
    width: 854px;
    height: 1200px;
    background: var(--paper);
  }
  .bag-print {
    position: relative;
    width: 854px;
    height: 1200px;
    background: var(--paper);
  }
  .slogan-box {
    position: absolute;
    left: 176px;
    top: 222px;
    width: 502px;
    height: 198px;
    background: var(--ink);
    color: var(--inverse);
    display: flex;
    flex-direction: column;
    justify-content: center;
    align-items: center;
    font-family: "Noto Sans JP", sans-serif;
    font-weight: 500;
    font-size: 46px;
    line-height: 1.45;
    letter-spacing: 0.02em;
    text-align: center;
  }
  .company-name {
    position: absolute;
    left: 0;
    top: 470px;
    width: 854px;
    margin: 0;
    text-align: center;
    font-family: "Zen Old Mincho", serif;
    font-weight: 900;
    font-size: 64px;
    line-height: 1.3;
    letter-spacing: 0.01em;
    color: var(--ink);
  }
  .truck-band {
    position: absolute;
    left: 176px;
    top: 612px;
    width: 502px;
    height: 192px;
    background: var(--brand-green);
  }
  .truck-illustration {
    position: absolute;
    left: 95px;
    top: 20px;
    width: 342px;
    height: 154px;
  }
  .english-message {
    position: absolute;
    left: 0;
    top: 838px;
    width: 854px;
    margin: 0;
    text-align: center;
    font-family: "EB Garamond", serif;
    font-style: italic;
    font-size: 31px;
    line-height: 1.3;
    color: var(--ink);
  }
</style>
</head>
<body>
  <main class="bag-print">
    <div class="slogan-box">
      <span>スマートな</span>
      <span>リサイクルカンパニー</span>
    </div>

    <h1 class="company-name">森川拓郎商会</h1>

    <div class="truck-band">
      <svg class="truck-illustration" viewBox="0 0 342 154" role="img" aria-label="会社のパッカー車（ごみ収集車）のイラスト">
        <rect x="0" y="0" width="342" height="154" rx="10" fill="var(--truck-tone)"/>
      </svg>
    </div>

    <p class="english-message">
      “Smart Recycle Company”<br>
      Leading to the solution of environmental problem<br>
      with Intelligence and Sense,<br>
      Creating A Sustainable Society Since 1946
    </p>
  </main>
</body>
</html>
```